Petal Sprite - web design for my new flower atelier

I would like to ask for design proposal for my newly established flower atelier. My brand name is Petal Sprite and I focus on realisation of events and flower projects (any kind) for physical as well as legel persons. I don’t operate as a standard flowershop. I would like to have 5 key parts - 1/Landing pg/welcome, 2/About me, 3/Gallery, 4/References, 5/Contact details. I would like the web design to reflect the way I am/ I do the things, ie, be slightly different, do non-tradiotional arrangements, my passion for flowers, gentle& fregile style, love for minimalism and details in the arrangements. I attach couple of photos of what I do so that you can better understand my style . You can see more on IG mirka_petal_sprite or FB Petal Sprite. I was wondering maybe one of the first 2 photos could be part of the landing pg. Or another idea is to have a design similar to this one https://thistlebloomstudio.example, ie to choose 3-5photos which are being animated like here. However, I am open to discuss any ideas and look forward for all the proposals.

Target Market(s)

physical as well as legal persons - weddings, celebrations, business events, projects for hotels, beaty salons, restaurants and others.. actually any kind of flower project

Industry/Entity Type

flowers

Number of Pages Required

1 page

Font styles to use
Other font styles liked:
• the font which matches the logo font style

Requirements
Must have
• to reflect the way I am as described above, I prefer more simple way of design, with the attention to a detail, I prefer pastel colours

```html
<!DOCTYPE html>
<html lang="en">
<head>
<meta charset="utf-8">
<title>Petal Sprite – Flower Atelier</title>
<link rel="stylesheet" href="https://fonts.googleapis.com/css2?family=Aladin&family=Questrial&family=Marcellus+SC&display=swap">
<style>
:root{
  --brown:#7d5d3b;
  --brown-dark:#6b4f33;
  --footer:#8b6a47;
  --cream:#f6ede4;
  --tan:#d8c3a5;
  --ink:#5a4a3a;
  --muted:#8a7a6a;
  --white:#ffffff;
  --hero-a:#3d3a2a;
  --hero-b:#a98a5a;
}
*{box-sizing:border-box;margin:0;padding:0}
html,body{width:1200px;height:4199px;overflow:hidden;background:var(--white)}
body{position:relative;font-family:"Questrial",sans-serif;color:var(--ink)}
.abs{position:absolute}
.script{font-family:"Aladin",cursive;font-weight:400}
.caps{font-family:"Marcellus SC",serif}

/* nav */
.nav{top:0;left:0;width:1200px;height:60px;background:var(--white);z-index:3}
.nav a{position:absolute;top:22px;font-size:12.5px;color:var(--ink);text-decoration:none}
.nav .active{left:316px;top:16px;width:69px;height:33px;border-radius:17px;background:var(--brown);color:var(--white);text-align:center;line-height:33px}
.nav-icon{position:absolute;top:17px;width:30px;height:30px;border:1.5px solid var(--brown);border-radius:50%}
.logo-disc{left:528px;top:-15px;width:144px;height:144px;border-radius:50%;background:var(--white);z-index:4;text-align:center}
.logo-disc .mark{width:30px;height:30px;border:1.5px solid var(--brown);border-radius:50%;margin:48px auto 8px}
.logo-name{font-family:"Aladin",cursive;font-size:20px;color:var(--brown)}

/* hero */
.hero{top:60px;left:0;width:1200px;height:652px;background:linear-gradient(100deg,var(--hero-a) 0%,#5b5134 40%,var(--hero-b) 75%,#c9b48c 100%)}
.hero-title{left:90px;top:240px;font-size:52px;line-height:54px;color:var(--white)}
.hero-title .soft{color:var(--tan)}
.hero-text{left:89px;top:428px;width:440px;font-size:13px;line-height:22.5px;color:var(--white)}
.slide-arrow{top:352px;width:42px;height:42px;border-radius:50%;background:rgba(120,95,60,.55)}

/* buttons */
.btn{position:absolute;height:41px;border-radius:21px;background:var(--brown);color:var(--white);font-family:"Marcellus SC",serif;font-size:14px;line-height:41px;padding-left:22px;letter-spacing:.5px}
.btn.ghost{background:transparent;border:1.5px solid var(--white)}
.btn svg{position:absolute;right:10px;top:8px}

/* about */
.about-bg{top:712px;left:0}
.about-kicker{left:200px;width:191px;top:793px;text-align:right;font-size:15px;color:var(--ink)}
.about-title{left:120px;width:271px;top:812px;text-align:right;font-size:50px;color:var(--brown)}
.about-text{left:519px;top:790px;width:430px;font-size:11.5px;line-height:21px;color:var(--muted)}
.about-text p+p{margin-top:14px}
.portrait{left:402px;top:1107px;width:320px;height:320px;border-radius:50%;background:radial-gradient(circle at 50% 40%,#b7a48a,#6f7a52 70%,#4c5a38)}

/* gallery */
.section-title{width:1200px;left:0;text-align:center;color:var(--brown);font-size:52px}
.gallery-sub{top:1600px;left:0;width:1200px;text-align:center;font-size:13.5px;line-height:23px;font-style:italic;color:var(--ink)}
.tile{width:274px;height:300px;border-radius:137px 137px 0 0}
.tile-frame{left:152px;top:1671px;width:288px;height:311px;border:1.5px solid var(--brown);border-radius:144px 144px 0 0}

/* references */
.refs{top:2445px;left:0;width:1200px;height:525px;background:linear-gradient(120deg,#2f2a22,#4d3f2c 45%,#6a5634 70%,#3a3226)}
.refs-sub{top:2576px;left:0;width:1200px;text-align:center;font-size:13px;color:var(--white)}
.ref-card{top:2642px;width:382px;height:196px;border-radius:24px;background:rgba(125,93,59,.88)}
.ref-card .avatar{position:absolute;left:25px;top:35px;width:74px;height:74px;border-radius:50%;background:radial-gradient(circle,#d7c2a3,#8b7358)}
.ref-card .q{position:absolute;left:17px;top:38px;font-family:"Aladin",cursive;font-size:22px;color:var(--white)}
.ref-card .quote{position:absolute;left:124px;top:36px;width:240px;font-size:13px;line-height:21px;font-style:italic;color:var(--white)}
.ref-card .name{position:absolute;left:124px;top:135px;font-family:"Aladin",cursive;font-size:17px;color:var(--white)}
.ref-card .name::before{content:"";display:inline-block;width:18px;height:1.5px;background:var(--white);vertical-align:middle;margin-right:9px}
.dot{top:2878px;height:3px;width:14px;background:var(--white)}

/* social */
.social-mark{left:584px;top:3053px;width:32px;height:32px;border:2.5px solid var(--brown);border-radius:50%}
.insta{top:3203px;width:162px;height:161px}

/* contact */
.contact-band{top:3505px;left:0;width:1200px;height:404px;background:var(--cream)}
.ask{font-family:"Aladin",cursive;font-size:19px;color:var(--ink)}
.ask-info{font-size:14px;font-weight:700;color:var(--brown)}
.news-sub{top:3742px;left:0;width:1200px;text-align:center;font-size:12.5px;color:var(--ink)}
.input{left:326px;top:3793px;width:420px;height:40px;border-radius:20px 0 0 20px;background:var(--white);font-size:11px;line-height:40px;padding-left:18px;color:var(--muted)}

/* footer */
.footer{top:3909px;left:0;width:1200px;height:290px;background:var(--footer);color:var(--white)}
.f-head{font-family:"Aladin",cursive;font-size:19px;position:absolute;top:48px}
.f-text{position:absolute;font-size:10.5px;line-height:21px}
.f-list{position:absolute;list-style:none;font-size:10.5px;line-height:24px}
.f-list li::before{content:"";display:inline-block;width:5px;height:5px;border:1px solid var(--white);border-radius:50%;margin-right:12px;vertical-align:middle}
.f-copy{position:absolute;top:258px;width:1200px;text-align:center;font-size:10px}
</style>
</head>
<body>

<header class="abs nav">
  <a class="active" href="#home">Home</a>
  <a style="left:403px" href="#about">About Me</a>
  <a style="left:481px" href="#gallery">Gallery</a>
  <a style="left:681px" href="#references">References</a>
  <a style="left:769px" href="#contact">Contact</a>
  <span class="nav-icon" style="left:833px">
    <svg width="27" height="27" viewBox="0 0 27 27" fill="none" stroke="#7d5d3b" stroke-width="1.4"><circle cx="13.5" cy="10.5" r="4"/><path d="M6.5 21c1-4 4-5.5 7-5.5s6 1.5 7 5.5"/></svg>
  </span>
  <span class="nav-icon" style="left:869px">
    <svg width="27" height="27" viewBox="0 0 27 27" fill="none" stroke="#7d5d3b" stroke-width="1.4"><rect x="6.5" y="8.5" width="14" height="10" rx="1"/><path d="M6.5 9l7 5.5 7-5.5"/></svg>
  </span>
</header>
<div class="abs logo-disc"><div class="mark"></div><div class="logo-name">Petal Sprite</div></div>

<section id="home" class="abs hero" role="img" aria-label="Woman holding a large bouquet of yellow, peach and orange ranunculus outdoors"></section>
<h1 class="abs script hero-title">Start Your<br><span class="soft">Unique Story With</span><br>Petal Sprite</h1>
<p class="abs hero-text">We are a flower studio. We create bouquets and Decorations with Respect to the Space, the Spirit of the Place and with Respect to your Unique Story.</p>
<a class="btn ghost" style="left:86px;top:508px;width:185px">CONTACT US
  <svg width="26" height="26" viewBox="0 0 26 26" fill="none" stroke="#fff" stroke-width="1.3"><circle cx="13" cy="13" r="11"/><path d="M2 13h14M12 9l4 4-4 4"/></svg></a>
<div class="abs slide-arrow" style="left:39px"><svg width="42" height="42" viewBox="0 0 42 42" fill="none" stroke="#fff" stroke-width="1.4"><path d="M24 15l-6 6 6 6"/></svg></div>
<div class="abs slide-arrow" style="left:1120px"><svg width="42" height="42" viewBox="0 0 42 42" fill="none" stroke="#fff" stroke-width="1.4"><path d="M18 15l6 6-6 6"/></svg></div>

<section id="about">
  <svg class="abs about-bg" width="1200" height="600" viewBox="0 0 1200 600">
    <polygon points="0,0 1200,0 1200,413 783,600 0,413" fill="#f6ede4"/>
    <ellipse cx="1000" cy="440" rx="90" ry="130" fill="#ece0d2" role="img" aria-label="Faint vase of flowers"/>
  </svg>
  <p class="abs about-kicker">Petal Sprite</p>
  <h2 class="abs script about-title">About Us</h2>
  <div class="abs about-text">
    <p>Lorem Ipsum has been the industry's standard dummy text ever since the 1500s, when an unknown printer too galley of type and scrambled it to make a type specimen book it has survived.</p>
    <p>Lorem Ipsum has been the industry's standard dummy text ever since the 1500s, when an unknown printer took a galley of type and scrambled it to make a type specimen book. It has survived not only five centuries, but also the leap into electronic typesetting, remaining essentially unchanged It was popularised.</p>
  </div>
  <a class="btn" style="left:522px;top:989px;width:182px">LEARN MORE
    <svg width="26" height="26" viewBox="0 0 26 26" fill="none" stroke="#fff" stroke-width="1.3"><circle cx="13" cy="13" r="11"/><path d="M2 13h14M12 9l4 4-4 4"/></svg></a>
  <svg class="abs" style="left:372px;top:1077px" width="380" height="380" viewBox="0 0 380 380" fill="none" stroke="#7d5d3b" stroke-width="3">
    <path d="M120 28 A175 175 0 0 0 150 360"/>
    <path d="M260 20 A175 175 0 0 1 225 357"/>
  </svg>
  <div class="abs portrait" role="img" aria-label="Florist holding two wrapped bouquets in a winter garden"></div>
</section>

<section id="gallery">
  <h2 class="abs script section-title" style="top:1518px">Gallery</h2>
  <p class="abs gallery-sub">We are a flower studio. We create bouquets &amp; Decorations with Respect to the Space,<br>the Spirit of the Place and with Respect to your Unique Story...</p>
  <div class="abs tile-frame"></div>
  <div class="abs tile" style="left:166px;top:1676px;background:linear-gradient(#6a4d38,#7b6a5a 45%,#58585c)" role="img" aria-label="Hanging autumn flower installation"></div>
  <div class="abs tile" style="left:463px;top:1676px;background:linear-gradient(#eceae6,#dcd8d0 70%,#c9c4ba)" role="img" aria-label="Curly willow and orange poppies in a green vase"></div>
  <div class="abs tile" style="left:760px;top:1676px;background:linear-gradient(#5a4332,#7d8a6a 50%,#9b9a94)" role="img" aria-label="Large white and green bouquet on a wooden deck"></div>
  <div class="abs tile" style="left:166px;top:2007px;background:linear-gradient(#e8ecef,#5f7452 50%,#e6e8ea)" role="img" aria-label="Green bouquet in a dark vase in snow"></div>
  <div class="abs tile" style="left:463px;top:2007px;background:linear-gradient(#b0765a,#7b6a4a 50%,#d9c9b5)" role="img" aria-label="Protea arrangement in front of a brick wall"></div>
  <div class="abs tile" style="left:760px;top:2007px;background:linear-gradient(#8c8a98,#b8a690 55%,#6f6a7a)" role="img" aria-label="Wrapped dried flower bouquet held outdoors"></div>
  <a class="btn" style="left:509px;top:2331px;width:182px">EXPLORE ALL
    <svg width="26" height="26" viewBox="0 0 26 26" fill="none" stroke="#fff" stroke-width="1.3"><circle cx="13" cy="13" r="11"/><path d="M2 13h14M12 9l4 4-4 4"/></svg></a>
</section>

<section id="references">
  <div class="abs refs" role="img" aria-label="Dim interior with a yellow armchair and a vase on a table"></div>
  <h2 class="abs script section-title" style="top:2515px;color:var(--white);font-size:50px">References</h2>
  <p class="abs refs-sub">What Our Client Say About Us</p>
  <article class="abs ref-card" style="left:202px">
    <div class="avatar" role="img" aria-label="Client photo"></div><span class="q">66</span>
    <p class="quote">" Lorem Ipsum has been the industry's standard dummy text ever since thwhen an unknown printer too galley type...."</p>
    <p class="name">Client Name</p>
  </article>
  <article class="abs ref-card" style="left:615px">
    <div class="avatar" role="img" aria-label="Client photo"></div><span class="q">66</span>
    <p class="quote">" Lorem Ipsum has been the industry's standard dummy text ever since thwhen an unknown printer too galley type...."</p>
    <p class="name">Client Name</p>
  </article>
  <span class="abs dot" style="left:590px"></span><span class="abs dot" style="left:610px;opacity:.6"></span>
</section>

<section id="social">
  <span class="abs social-mark"></span>
  <h2 class="abs script section-title" style="top:3095px">mirka_petal_sprite</h2>
  <div class="abs insta" style="left:183px;background:linear-gradient(#8a6a2a,#e0b22a 50%,#c0bdb5)" role="img" aria-label="Sunflower bouquet"></div>
  <div class="abs insta" style="left:350px;background:linear-gradient(#5b7a3a,#d8cfc4 60%,#7a9a4a)" role="img" aria-label="Girl holding a bouquet in a garden"></div>
  <div class="abs insta" style="left:520px;background:linear-gradient(#b4b2aa,#6a7a5a 50%,#8a7a6a)" role="img" aria-label="Child holding a wildflower bouquet"></div>
  <div class="abs insta" style="left:688px;background:linear-gradient(#8a7250,#c9a24a 50%,#a59a80)" role="img" aria-label="Sunflowers laid on a wooden table"></div>
  <div class="abs insta" style="left:857px;background:linear-gradient(#4a6a3a,#c9746a 50%,#5a7a3e)" role="img" aria-label="Garden flower bed in bloom"></div>
  <a class="btn" style="left:515px;top:3389px;width:168px">FOLLOW US
    <svg width="26" height="26" viewBox="0 0 26 26" fill="none" stroke="#fff" stroke-width="1.3"><circle cx="13" cy="13" r="11"/><path d="M2 13h14M12 9l4 4-4 4"/></svg></a>
</section>

<section id="contact">
  <div class="abs contact-band"></div>
  <p class="abs ask" style="left:346px;top:3572px">Have Question ?</p>
  <p class="abs ask-info" style="left:330px;top:3603px">info@PetalSprite.example</p>
  <svg class="abs" style="left:522px;top:3568px" width="36" height="28" viewBox="0 0 36 28" fill="none" stroke="#7d5d3b" stroke-width="1.5"><rect x="1" y="1" width="34" height="26" rx="2"/><path d="M1 2l17 14L35 2M1 27l12-12M35 27L23 15"/></svg>
  <span class="abs" style="left:601px;top:3554px;width:1px;height:78px;background:#d9c9b5"></span>
  <svg class="abs" style="left:646px;top:3570px" width="30" height="30" viewBox="0 0 30 30" fill="none" stroke="#7d5d3b" stroke-width="1.5"><path d="M6 2l5 6-3 4c2 4 6 8 10 10l4-3 6 5-3 4C14 28 2 16 2 5z"/></svg>
  <p class="abs ask" style="left:707px;top:3572px">Call Us On ?</p>
  <p class="abs ask-info" style="left:707px;top:3603px">+(0) 123 456 7890</p>
  <h2 class="abs script section-title" style="top:3680px;font-size:50px">Newsletter</h2>
  <p class="abs news-sub">Would you like to receive our exclusive update for signup !</p>
  <div class="abs input">Enter Email *</div>
  <a class="btn" style="left:706px;top:3793px;width:168px;height:40px;line-height:40px">SUBSCRIBE
    <svg width="26" height="26" viewBox="0 0 26 26" fill="none" stroke="#fff" stroke-width="1.3" style="top:7px"><circle cx="13" cy="13" r="11"/><path d="M2 13h14M12 9l4 4-4 4"/></svg></a>
</section>

<footer class="abs footer">
  <span class="abs" style="left:153px;top:46px;width:60px;height:60px;border:1.5px solid var(--white);border-radius:50%"></span>
  <p class="abs logo-name" style="left:122px;top:112px;color:var(--white);font-size:24px">Petal Sprite</p>
  <span class="abs" style="left:156px;top:152px;width:16px;height:16px;border:1.5px solid var(--white);border-radius:50%"></span>
  <span class="abs" style="left:182px;top:152px;width:16px;height:16px;border:1.5px solid var(--white);border-radius:3px"></span>

  <h3 class="f-head" style="left:336px">Contact Us</h3>
  <p class="f-text" style="left:336px;top:92px">Phone : &nbsp;+(0) 123 456 7890</p>
  <p class="f-text" style="left:336px;top:121px">Email : &nbsp;info@PetalSprite.example</p>
  <p class="f-text" style="left:336px;top:150px">Address : City, country Street<br><span style="padding-left:53px">lorem ipsum simple text</span></p>

  <h3 class="f-head" style="left:611px">About Us</h3>
  <p class="f-text" style="left:611px;top:92px;width:240px">We are a flower studio. We create bouquets &amp; Decorations with Respect to the Space, the Spirit of the Place and with Respect to your Unique Story...</p>

  <h3 class="f-head" style="left:887px">Information</h3>
  <ul class="f-list" style="left:887px;top:88px">
    <li>Search</li><li>Location</li><li>Privacy Policy</li><li>Contact Us</li><li>Newsletter</li>
  </ul>
  <p class="f-copy">©2022 Petal Sprite - All rights reserved.</p>
</footer>

</body>
</html>
```